New business card for UK roofing company

We are Brindmore Roofing and we need a business card design for our staff.

We offer the following services:

- New roofs
- General roof repairs
- Drone surveys
- Single ply roofing
- Steel cladding
- Asbestos removal
- Electronic leak detection

I have attached our logo. I have also attached example branding printed to our vans. The business card should fit in with the style of our branding.

The business card should have the following information;

Address:
Unit 17c Wendlecroft Farm
Wendlecroft Lane
Hatchington
CM4 9QD

Telephone: 020 7946 0372
24 Hour: 0800 612 4479

Email: ray@brindmoreroofing.example
Mobile: 07700981234
Name: Ray Tunstead
Website: www.brindmoreroofing.example

The business card will be printed in Spot UV, see here: https://www.kestaprint.example/business-cards/spot-uv/

If you need anymore info, please let me know,

```html
<!DOCTYPE html>
<html lang="en">
<head>
<meta charset="utf-8">
<title>Brindmore Roofing – Business Card</title>
<link rel="stylesheet" href="https://fonts.googleapis.com/css2?family=Barlow:wght@500;600&family=Poppins:wght@400;600;700&display=swap">
<style>
  :root {
    --navy: #143d69;
    --navy-deep: #0f3259;
    --emboss: #0d2f52;
    --cyan: #05aedb;
    --white: #ffffff;
    --ink: #173a63;
    --backdrop: #c5c6c8;
  }
  * { margin: 0; padding: 0; box-sizing: border-box; }
  html, body { width: 900px; height: 1200px; overflow: hidden; }
  body { background: var(--backdrop); position: relative; font-family: "Poppins", sans-serif; }

  .card {
    position: absolute; left: 164px; width: 573px; height: 369px;
    border-radius: 28px; overflow: hidden; background: var(--navy);
  }
  .card--front { top: 208px; }
  .card--back { top: 623px; }

  /* Front */
  .front-mark {
    position: absolute; left: 256px; top: 118px; width: 60px; height: 60px;
    border-radius: 50%; border: 3px solid var(--emboss);
  }
  .front-name {
    position: absolute; left: 0; right: 0; top: 186px; text-align: center;
    font-family: "Poppins", sans-serif; font-weight: 600; font-size: 40px;
    letter-spacing: -1.5px; color: var(--emboss); line-height: 1;
  }
  .services {
    position: absolute; left: 0; right: 0; top: 291px; text-align: center;
    font-family: "Barlow", sans-serif; font-weight: 600; font-size: 15px;
    letter-spacing: 0.6px; color: var(--white); line-height: 22.5px;
  }
  .services .sep { color: var(--cyan); padding: 0 3px; }

  /* Back */
  .back-bg { position: absolute; inset: 0; width: 100%; height: 100%; }
  .person { position: absolute; left: 25px; top: 44px; }
  .person-name {
    font-weight: 700; font-size: 25px; color: var(--cyan);
    letter-spacing: 0.5px; line-height: 1;
  }
  .person-role {
    font-weight: 400; font-size: 14.5px; color: var(--white);
    letter-spacing: 1px; margin-top: 5px;
  }
  .contact-list { position: absolute; left: 25px; top: 116px; width: 232px; list-style: none; }
  .contact-list li {
    display: flex; align-items: center; gap: 6px; height: 24px;
    font-size: 11.5px; color: var(--white); letter-spacing: 0.1px; white-space: nowrap;
  }
  .contact-list svg, .phones svg { width: 13px; height: 13px; flex: none; }
  .address {
    position: absolute; left: 266px; top: 94px; font-style: normal;
    font-size: 14px; color: var(--white); line-height: 23.5px; letter-spacing: 0.3px;
  }
  .back-logo {
    position: absolute; left: 25px; top: 253px; display: flex; align-items: center; gap: 8px;
  }
  .back-logo .dot { width: 28px; height: 28px; border-radius: 50%; background: var(--cyan); }
  .back-logo .wordmark {
    font-weight: 600; font-size: 25px; letter-spacing: -1px; color: var(--ink); line-height: 1;
  }
  .phones { position: absolute; left: 25px; top: 293px; list-style: none; }
  .phones li {
    display: flex; align-items: center; gap: 8px; height: 23.5px;
    font-size: 15px; letter-spacing: 3px; color: var(--ink);
  }
  .phones .note { color: var(--cyan); letter-spacing: 1px; margin-left: -6px; }
</style>
</head>
<body>

<section class="card card--front" aria-label="Business card front">
  <div class="front-mark"></div>
  <div class="front-name">brindmoreroofing</div>
  <p class="services">
    New roofs<span class="sep">|</span>General<span class="sep">|</span>roof repairs<span class="sep">|</span>Drone surveys<span class="sep">|</span>Single ply roofing<br>
    Steel cladding<span class="sep">|</span>Asbestos removal<span class="sep">|</span>Electronic leak detection
  </p>
</section>

<section class="card card--back" aria-label="Business card back">
  <svg class="back-bg" viewBox="0 0 573 369" preserveAspectRatio="none" aria-hidden="true">
    <rect width="573" height="369" fill="var(--navy)"/>
    <polygon points="0,230 330,195 573,180 573,369 0,369" fill="var(--cyan)"/>
    <polygon points="0,246 573,198 573,369 0,369" fill="var(--white)"/>
    <line x1="0" y1="246" x2="573" y2="198" stroke="var(--navy-deep)" stroke-width="2"/>
    <circle cx="520" cy="250" r="128" fill="var(--cyan)" stroke="var(--white)" stroke-width="8"/>
  </svg>

  <div class="person">
    <div class="person-name">RAY TUNSTEAD</div>
    <div class="person-role">Director</div>
  </div>

  <ul class="contact-list">
    <li>
      <svg viewBox="0 0 12 14"><rect x="2" y="0.8" width="8" height="12.4" rx="1.5" fill="none" stroke="var(--cyan)" stroke-width="1.5"/><circle cx="6" cy="11" r="0.9" fill="var(--cyan)"/></svg>
      07700 981 234
    </li>
    <li>
      <svg viewBox="0 0 14 14"><rect x="0.5" y="3" width="13" height="8.5" rx="1" fill="var(--cyan)"/><path d="M1 3.5 L7 8 L13 3.5" fill="none" stroke="var(--navy)" stroke-width="1.2"/></svg>
      ray@brindmoreroofing.example
    </li>
    <li>
      <svg viewBox="0 0 14 14"><circle cx="7" cy="7" r="6" fill="none" stroke="var(--cyan)" stroke-width="1.3"/><ellipse cx="7" cy="7" rx="2.6" ry="6" fill="none" stroke="var(--cyan)" stroke-width="1.1"/><line x1="1" y1="7" x2="13" y2="7" stroke="var(--cyan)" stroke-width="1.1"/></svg>
      www.brindmoreroofing.example
    </li>
  </ul>

  <address class="address">
    Unit 17c Wendlecroft Farm<br>
    Wendlecroft Lane<br>
    Hatchington<br>
    CM4 9QD
  </address>

  <div class="back-logo">
    <span class="dot"></span>
    <span class="wordmark">brindmoreroofing</span>
  </div>

  <ul class="phones">
    <li>
      <svg viewBox="0 0 14 14"><path d="M3 1 L5.5 3.5 L4 5.5 C5 7.5 6.5 9 8.5 10 L10.5 8.5 L13 11 L11.5 13 C6 13 1 8 1 2.5 Z" fill="var(--cyan)"/></svg>
      020 7946 0372
    </li>
    <li>
      <svg viewBox="0 0 14 14"><path d="M3 1 L5.5 3.5 L4 5.5 C5 7.5 6.5 9 8.5 10 L10.5 8.5 L13 11 L11.5 13 C6 13 1 8 1 2.5 Z" fill="var(--cyan)"/></svg>
      0800 612 4479 <span class="note">(24 Hour)</span>
    </li>
  </ul>
</section>

</body>
</html>
```